Desk Allies Business Card

Contact Information for Business Card

Janne Voutilainen
Managing Director

3/47 Brindle Street Fernbrook ACT 2915

Tel: +61 02 6257 3140
Mob: +61 0427 315 846

Email: janne@deskallies.com.au
Web: www.deskallies.com.au

Colors

Designer to choose colors to be used in the design.

Requirements
Must have
• Logo, Name, Title, Address, Telephone, Mobile, Email Address and Website
• "Desk Ally International Pty Ltd"

```html
<!DOCTYPE html>
<html lang="en">
<head>
<meta charset="utf-8">
<title>Desk Allies Business Card</title>
<link rel="stylesheet" href="https://fonts.googleapis.com/css2?family=Montserrat:wght@400;500;600;700&display=swap">
<style>
  :root {
    --backdrop: #e3e4e6;
    --card: #ffffff;
    --brand-blue: #1a73c2;
    --ink: #1d1d1f;
    --ink-soft: #3a3a3c;
    --hatch: #ececee;
  }
  * { box-sizing: border-box; margin: 0; padding: 0; }
  html, body { width: 1200px; height: 800px; overflow: hidden; }
  body {
    background: var(--backdrop);
    font-family: "Montserrat", sans-serif;
    position: relative;
  }
  .card {
    position: absolute;
    top: 250px;
    width: 525px;
    height: 300px;
    background: var(--card);
    box-shadow: 0 10px 30px rgba(0,0,0,0.12);
    overflow: hidden;
  }
  .card--front { left: 50px; }
  .card--back { left: 625px; }

  .corner-band {
    position: absolute;
    right: 0;
    bottom: 0;
    width: 150px;
    height: 70px;
    background: var(--hatch);
  }

  /* Front */
  .brand {
    position: absolute;
    left: 70px;
    top: 95px;
    display: flex;
    align-items: center;
    gap: 16px;
  }
  .brand__dot {
    width: 44px;
    height: 44px;
    border-radius: 50%;
    background: var(--brand-blue);
    flex: none;
  }
  .brand__name {
    color: var(--brand-blue);
    font-weight: 600;
    font-size: 40px;
    letter-spacing: 1px;
    text-transform: uppercase;
    line-height: 1;
    white-space: nowrap;
  }
  .brand__tagline {
    position: absolute;
    left: 130px;
    top: 148px;
    font-size: 12px;
    letter-spacing: 3.2px;
    color: var(--ink-soft);
    text-transform: uppercase;
    white-space: nowrap;
  }
  .legal-name {
    position: absolute;
    left: 30px;
    bottom: 30px;
    font-size: 16px;
    color: var(--ink);
    white-space: nowrap;
  }

  /* Back */
  .person {
    position: absolute;
    left: 40px;
    top: 36px;
  }
  .person__name {
    font-weight: 600;
    font-size: 24px;
    text-transform: uppercase;
    color: var(--ink);
    letter-spacing: 0.5px;
    white-space: nowrap;
  }
  .person__title {
    font-weight: 600;
    font-size: 13px;
    color: var(--ink);
    margin-top: 2px;
  }
  .address {
    position: absolute;
    left: 40px;
    top: 100px;
    font-size: 13px;
    color: var(--ink-soft);
    white-space: nowrap;
  }
  .contact-list {
    position: absolute;
    left: 40px;
    top: 132px;
    list-style: none;
    font-size: 13px;
    line-height: 22px;
    color: var(--ink-soft);
    white-space: nowrap;
  }
  .contact-list__label {
    display: inline-block;
    width: 26px;
    color: var(--brand-blue);
    font-weight: 600;
  }
  .back-brand {
    position: absolute;
    right: 40px;
    top: 110px;
    display: flex;
    flex-direction: column;
    align-items: center;
    gap: 10px;
  }
  .back-brand__dot {
    width: 60px;
    height: 60px;
    border-radius: 50%;
    background: var(--brand-blue);
  }
  .back-brand__name {
    color: var(--brand-blue);
    font-weight: 600;
    font-size: 16px;
    text-transform: uppercase;
    letter-spacing: 1px;
    white-space: nowrap;
  }
</style>
</head>
<body>
  <section class="card card--front">
    <div class="brand">
      <span class="brand__dot"></span>
      <span class="brand__name">Desk Allies</span>
    </div>
    <p class="brand__tagline">Healthy Workplace Environments</p>
    <p class="legal-name">Desk Ally International Pty Ltd</p>
    <div class="corner-band" role="img" aria-label="Light grey diagonal line texture"></div>
  </section>

  <section class="card card--back">
    <div class="person">
      <h1 class="person__name">Janne Voutilainen</h1>
      <p class="person__title">Managing Director</p>
    </div>
    <p class="address">3/47 Brindle Street Fernbrook ACT 2915</p>
    <ul class="contact-list">
      <li><span class="contact-list__label">T:</span>+61 02 6257 3140</li>
      <li><span class="contact-list__label">M:</span>+61 0427 315 846</li>
      <li><span class="contact-list__label">E:</span>janne@deskallies.com.au</li>
      <li><span class="contact-list__label">W:</span>www.deskallies.com.au</li>
    </ul>
    <div class="back-brand">
      <span class="back-brand__dot"></span>
      <span class="back-brand__name">Desk Allies</span>
    </div>
    <div class="corner-band" role="img" aria-label="Light grey diagonal line texture"></div>
  </section>
</body>
</html>
```